Web App Dashboard Design for Healthcare Company

We have developed a simple web application with 3 navigation menus. We like the current design (very much modeled after Ledgerly), but we want to explore UI options for the branding, header, menus, and footer that we may not have considered.

The attached screenshots show the layout and two menu "hover" views as they currently exist.

This web application is used by employees only.

Menu 1 - Module Menu:
Allows the user to switch easily between Account, Employee, and Care Management.

Menu 2 - Reports Menu
Allows user to view available reports within each Module.

Menu 3 - Admin Menu
Allows the user to easily create new content types within each module.

Use our branded colors and font.

Colors:
Logo Blue (dark): 00c0f3
Logo Blue (light): 44c8f5
Nav Blue: 0994d0
Green: 71b44b
Grayscale: (not specified)

Font:
Lato (Google Font)

Target Market(s)

Internal staff.

Industry/Entity Type

Healthcare

Number of Pages Required

3 page

Font styles to use
Sans Serif
Other font styles liked:
• Lato (Google Font)

Colors
0293ce
9bcb3c

Requirements
Must have
• It's really a one page design, but we want to see the two "hover" views for the Module Menu and the Admin Menu.
• It should also be very clear which "Report" page the user is on (the active menu link).
• Must use branded colors, font, and logo.
• Logo Blue (dark): 00c0f3
• Logo Blue (light): 44c8f5
• Nav Blue: 0994d0
• Green: 71b44b
• Grayscale: Designer may choose
Nice to have
• It would be nice to have simple uncluttered payouts.
Should not have
• The design should not have menu options exposed by default.

```html
<!DOCTYPE html>
<html lang="en">
<head>
<meta charset="utf-8">
<title>Pathwise – Account Management</title>
<link href="https://fonts.googleapis.com/css2?family=Lato:ital,wght@0,400;0,700;1,400&display=swap" rel="stylesheet">
<style>
:root{
  --nav-blue:#0994d0;
  --logo-blue:#44c8f5;
  --icon-blue:#5bc3ee;
  --green:#71b44b;
  --ink:#222;
  --muted:#555;
  --line:#d6d6d6;
  --canvas:#e6e6e6;
  --row-alt:#f4f6f8;
  --footer:#2e2e2e;
  --white:#fff;
  --badge-red:#f0605a;
}
*{box-sizing:border-box;margin:0;padding:0}
html,body{width:1200px;height:694px;overflow:hidden}
body{font-family:'Lato',sans-serif;color:var(--ink);background:var(--canvas);position:relative}

.sidebar{position:absolute;left:0;top:0;width:233px;height:656px;background:var(--white);border-right:1px solid var(--line)}
.brand{height:99px;display:flex;align-items:center;justify-content:center;gap:8px}
.brand-mark{width:14px;height:14px;background:var(--logo-blue)}
.brand-name{font-size:26px;font-weight:700;color:var(--ink)}
.search{position:absolute;top:128px;left:0;width:233px;height:28px;border-bottom:1px solid #9a9a9a;display:flex;align-items:center;padding:0 12px 0 43px;justify-content:space-between}
.search span{font-size:12px;font-style:italic;color:#666}
.nav{position:absolute;top:177px;left:0;width:233px;list-style:none}
.nav-item{display:flex;flex-direction:column;align-items:center;justify-content:center;gap:6px;border-bottom:1px solid var(--line);font-size:15px;font-weight:700;color:#333}
.nav-item svg{width:22px;height:22px;fill:var(--icon-blue)}
.nav-item.is-active{background:var(--green);color:var(--white);border-bottom:none}
.nav-item.is-active svg{fill:var(--white)}

.topbar{position:absolute;left:234px;top:0;width:966px;height:99px;background:var(--white);border-bottom:1px solid #cfcfcf}
.module-select{position:absolute;left:18px;top:36px;width:205px;height:27px;border:2px solid #9a9a9a;display:flex;align-items:center;justify-content:space-between;padding:0 8px 0 10px;font-size:12px;font-style:italic}
.icon-btn{position:absolute;top:44px;width:16px;height:16px}
.icon-btn .count{position:absolute;right:-5px;top:-5px;width:9px;height:9px;border-radius:50%;font-size:6px;color:var(--white);text-align:center;line-height:9px}
.user{position:absolute;left:710px;top:35px;line-height:1.3}
.user-name{font-size:12px}
.user-role{font-size:10px;color:#333}
.avatar{position:absolute;left:773px;top:28px;width:44px;height:44px;border-radius:50%;background:radial-gradient(circle at 50% 40%,#b07a5e,#4a2a22)}
.logout{position:absolute;left:854px;top:41px;display:flex;align-items:center;gap:6px;font-size:14px;color:#555}

.data-panel{position:absolute;left:253px;top:126px;width:903px}
.data-table{width:100%;border-collapse:collapse;table-layout:fixed;font-size:11px;text-align:center}
.data-table th{background:var(--nav-blue);color:var(--white);font-weight:700;height:41px;border-right:1px solid #37a7da}
.data-table td{height:41.7px;background:var(--white);border-right:1px solid #e4e4e4}
.data-table tr:nth-child(even) td{background:var(--row-alt)}
.data-table th:last-child,.data-table td:last-child{border-right:none}
.tag{display:inline-block;width:101px;padding:3px 0;color:var(--white);font-size:11px}
.tag.green{background:var(--green)}
.tag.blue{background:var(--nav-blue)}
.status{color:var(--green)}
.scrollbar{position:absolute;right:4px;top:50px;width:5px;height:408px;background:#e4e4e4}
.scrollbar i{display:block;height:70px;background:#b5b5b5;border-radius:2px}

.pager{position:absolute;left:631px;top:607px;display:flex;align-items:center;gap:11px;font-size:12px;color:#444}
.pager .circle{width:21px;height:21px;border:1px solid #777;border-radius:50%;display:flex;align-items:center;justify-content:center;font-size:10px}

.footer{position:absolute;left:0;top:656px;width:1200px;height:38px;background:var(--footer);color:var(--white);display:flex;align-items:center;justify-content:space-between;padding:0 46px 0 51px;font-size:12.5px}
</style>
</head>
<body>
<aside class="sidebar">
  <div class="brand"><span class="brand-mark"></span><span class="brand-name">Pathwise</span></div>
  <div class="search"><span>Search</span>
    <svg width="15" height="15" viewBox="0 0 16 16" fill="none" stroke="#666" stroke-width="1.6"><circle cx="6.5" cy="6.5" r="5"/><path d="M10.5 10.5l4 4"/></svg>
  </div>
  <ul class="nav">
    <li class="nav-item is-active" style="height:74px"><svg viewBox="0 0 24 24"><path d="M12 2a2 2 0 0 1 2 2v.5A6.5 6.5 0 0 1 18.5 11v5l2 2.5h-17l2-2.5v-5A6.5 6.5 0 0 1 10 4.5V4a2 2 0 0 1 2-2zm-2.5 18h5a2.5 2.5 0 0 1-5 0z"/></svg>Reminders</li>
    <li class="nav-item" style="height:81px"><svg viewBox="0 0 24 24"><circle cx="12" cy="7" r="5"/><path d="M2 22c0-6 4.5-9 10-9s10 3 10 9z"/></svg>Accounts</li>
    <li class="nav-item" style="height:79px"><svg viewBox="0 0 24 24"><path d="M8 2h8v4h-2V4h-4v2H8z"/><path d="M2 6h20v16H2zm8 4v3H7v3h3v3h4v-3h3v-3h-3v-3z"/></svg>Patient Requests</li>
    <li class="nav-item" style="height:79px"><svg viewBox="0 0 24 24"><path d="M4 1h11l5 5v17H4zm3 8v1.5h10V9zm0 4v1.5h10V13zm0 4v1.5h10V17z"/></svg>Reports</li>
    <li class="nav-item" style="height:81px;border-bottom:none"><svg viewBox="0 0 24 24"><path d="M8 3h8v3h-2V5h-4v1H8z"/><path d="M1 7h22v5H1zM1 13h22v9H1z"/></svg>My Company</li>
  </ul>
</aside>

<header class="topbar">
  <div class="module-select">Account Management
    <svg width="12" height="7" viewBox="0 0 12 7"><path d="M0 0h12L6 7z" fill="#555"/></svg>
  </div>
  <div class="icon-btn" style="left:605px">
    <svg viewBox="0 0 24 24" width="16" height="16" fill="#666"><path d="M12 2a2 2 0 0 1 2 2v.5A6.5 6.5 0 0 1 18.5 11v5l2 2.5h-17l2-2.5v-5A6.5 6.5 0 0 1 10 4.5V4a2 2 0 0 1 2-2zm-2.5 18h5a2.5 2.5 0 0 1-5 0z"/></svg>
    <span class="count" style="background:var(--logo-blue)">3</span>
  </div>
  <div class="icon-btn" style="left:642px">
    <svg viewBox="0 0 24 24" width="16" height="16" fill="#666"><path d="M1 5h22v15H1zm2 2v1l9 6 9-6V7l-9 6z"/></svg>
    <span class="count" style="background:var(--badge-red)">3</span>
  </div>
  <div class="user"><div class="user-name">Marcus L</div><div class="user-role">HR Admin</div></div>
  <div class="avatar" role="img" aria-label="User profile photo"></div>
  <div class="logout">
    <svg width="15" height="15" viewBox="0 0 16 16" fill="none" stroke="#555" stroke-width="1.4"><path d="M9 1H2v14h7M6 8h9M12 5l3 3-3 3"/></svg>Log out
  </div>
</header>

<main class="data-panel">
  <table class="data-table">
    <colgroup><col style="width:132px"><col style="width:132px"><col style="width:69px"><col style="width:180px"><col style="width:118px"><col style="width:168px"><col style="width:104px"></colgroup>
    <thead><tr><th>Name</th><th>Designation</th><th>Loremde</th><th>Email</th><th>Dolor Ipsum</th><th>Tablecraft</th><th></th></tr></thead>
    <tbody>
      <tr><td><span class="tag green">Nimbus Admin v1</span></td><td>Donec Non Gravida</td><td>Gravida</td><td>Dana R. Whitfield</td><td>Eleifend</td><td>Dana R. Whitfield</td><td class="status">Eleifend</td></tr>
      <tr><td><span class="tag green">Nimbus Admin v1</span></td><td>Donec Non Gravida</td><td>Gravida</td><td>Dana R. Whitfield</td><td>Eleifend</td><td>Dana R. Whitfield</td><td class="status">Eleifend</td></tr>
      <tr><td><span class="tag green">Nimbus Admin v1</span></td><td>Donec Non Gravida</td><td>Gravida</td><td>Dana R. Whitfield</td><td>Eleifend</td><td>Dana R. Whitfield</td><td class="status">Eleifend</td></tr>
      <tr><td><span class="tag green">Nimbus Admin v1</span></td><td>Donec Non Gravida</td><td>Gravida</td><td>Dana R. Whitfield</td><td>Eleifend</td><td>Dana R. Whitfield</td><td class="status">Eleifend</td></tr>
      <tr><td><span class="tag blue">Nimbus Admin v1</span></td><td>Donec Non Gravida</td><td>Gravida</td><td>Dana R. Whitfield</td><td>Eleifend</td><td>Dana R. Whitfield</td><td class="status">Eleifend</td></tr>
      <tr><td><span class="tag blue">Nimbus Admin v1</span></td><td>Donec Non Gravida</td><td>Gravida</td><td>Dana R. Whitfield</td><td>Eleifend</td><td>Dana R. Whitfield</td><td class="status">Eleifend</td></tr>
      <tr><td><span class="tag blue">Nimbus Admin v1</span></td><td>Donec Non Gravida</td><td>Gravida</td><td>Dana R. Whitfield</td><td>Eleifend</td><td>Dana R. Whitfield</td><td class="status">Eleifend</td></tr>
      <tr><td><span class="tag blue">Nimbus Admin v1</span></td><td>Donec Non Gravida</td><td>Gravida</td><td>Dana R. Whitfield</td><td>Eleifend</td><td>Dana R. Whitfield</td><td class="status">Eleifend</td></tr>
      <tr><td><span class="tag blue">Nimbus Admin v1</span></td><td>Donec Non Gravida</td><td>Gravida</td><td>Dana R. Whitfield</td><td>Eleifend</td><td>Dana R. Whitfield</td><td class="status">Eleifend</td></tr>
      <tr><td><span class="tag blue">Nimbus Admin v1</span></td><td>Donec Non Gravida</td><td>Gravida</td><td>Dana R. Whitfield</td><td>Eleifend</td><td>Dana R. Whitfield</td><td class="status">Eleifend</td></tr>
    </tbody>
  </table>
  <div class="scrollbar"><i></i></div>
</main>

<nav class="pager">
  <span class="circle">&laquo;</span><span class="circle">1</span><span>2</span><span>3</span><span>4</span><span class="circle">&raquo;</span>
</nav>

<footer class="footer">
  <span>Copyright © 2017 Pathwise.&nbsp; All Rights Reserved.</span>
  <span>Contact Us</span>
</footer>
</body>
</html>
```